Trendy, rustic, patriotic Facebook Design!

Would like something to catch people's eye! Must include our logo and phone number. 410-587-3920. Dogs in the project are a must. Bold pricing, location, etc to catch peoples eyes is a plus.

Target Market(s)

Dog owners

Font styles to use
Serif
Sans Serif

Colors
1f66ae
ec1f27
ffffff

Requirements
Must have
• Dogs, company logo, business phone 410-587-3920 and website www.furlowpaws.com
Nice to have
• Something that is rustic, trendy!
Should not have
• Cartoons.

```html
<!DOCTYPE html>
<html lang="en">
<head>
<meta charset="utf-8">
<title>Furlow Paws – Dog Training</title>
<link rel="stylesheet" href="https://fonts.googleapis.com/css2?family=Comic+Neue:wght@700&family=Open+Sans:wght@800&family=Roboto:wght@900&display=swap">
<style>
  :root {
    --blue: #1f66ae;
    --red: #ec1f27;
    --navy: #0f2f6b;
    --white: #ffffff;
    --peach-top: #f8bf68;
    --peach-bottom: #fbd291;
    --orange: #f6aa43;
    --box-line: #f5b04c;
  }
  * { margin: 0; padding: 0; box-sizing: border-box; }
  html, body { width: 1200px; height: 1200px; overflow: hidden; }
  body { background: var(--peach-bottom); }
  .poster {
    position: relative;
    width: 1200px;
    height: 1200px;
    overflow: hidden;
    background: linear-gradient(180deg, var(--peach-top) 0%, var(--peach-bottom) 100%);
  }
  .edge-line { position: absolute; left: 0; width: 100%; height: 10px; background: var(--blue); }
  .edge-line.top { top: 0; }
  .edge-line.bottom { bottom: 0; }
  .band { position: absolute; background: var(--red); }
  .band.top { left: 398px; right: 0; top: 10px; height: 70px; }
  .band.bottom { left: 0; right: 0; bottom: 10px; height: 75px; }
  .corner-disc {
    position: absolute;
    left: -211px; top: -217px;
    width: 608px; height: 608px;
    border-radius: 50%;
    background: radial-gradient(circle at 60% 40%, #f8b252 0%, var(--orange) 100%);
  }
  .brand {
    position: absolute;
    left: 20px; top: 130px;
    width: 300px;
    display: flex;
    align-items: center;
    gap: 12px;
  }
  .brand-dot { width: 34px; height: 34px; border-radius: 50%; background: var(--navy); flex: none; }
  .brand-name {
    font-family: "Open Sans", sans-serif;
    font-weight: 800;
    font-size: 38px;
    color: var(--navy);
    line-height: 1;
  }
  .dog-photo {
    position: absolute;
    left: 345px; top: 90px;
    width: 505px; height: 1025px;
    border-radius: 220px 220px 40px 40px;
    background: linear-gradient(180deg, rgba(214,150,90,0.55) 0%, rgba(245,236,222,0.7) 35%, rgba(205,140,80,0.55) 70%, rgba(240,225,200,0.35) 100%);
  }
  .headline { position: absolute; left: 0; top: 0; width: 1200px; height: 1200px; pointer-events: none; }
  .headline text { font-family: "Roboto", sans-serif; font-weight: 900; }
  .headline .word-dog { fill: var(--blue); }
  .headline .word-training { fill: var(--red); }
  .info-box {
    position: absolute;
    left: 753px; width: 433px;
    border: 2px solid var(--box-line);
    border-radius: 14px;
    text-align: center;
  }
  .info-box.call { top: 99px; height: 153px; }
  .info-box.web { top: 899px; height: 154px; }
  .info-label {
    font-family: "Comic Neue", cursive;
    font-weight: 700;
    color: var(--blue);
    font-size: 58px;
    line-height: 1;
  }
  .call .info-label { margin-top: 14px; }
  .web .info-label { margin-top: 20px; }
  .phone {
    font-family: "Open Sans", sans-serif;
    font-weight: 800;
    color: var(--red);
    font-size: 54px;
    line-height: 1;
    margin-top: 10px;
  }
  .site {
    font-family: "Open Sans", sans-serif;
    font-weight: 800;
    color: var(--red);
    font-size: 29px;
    line-height: 1;
    margin-top: 30px;
  }
</style>
</head>
<body>
<main class="poster">
  <div class="edge-line top"></div>
  <div class="band top"></div>
  <div class="corner-disc"></div>
  <div class="brand">
    <span class="brand-dot"></span>
    <span class="brand-name">Furlow Paws</span>
  </div>

  <div class="dog-photo" role="img" aria-label="Photo of a tan and white beagle standing on its hind legs, paws raised, looking up happily"></div>

  <svg class="headline" viewBox="0 0 1200 1200" aria-label="Dog Training">
    <text class="word-dog" x="720" y="596" font-size="245" textLength="463" lengthAdjust="spacingAndGlyphs">DOG</text>
    <text class="word-training" x="19" y="825" font-size="226" textLength="1164" lengthAdjust="spacing">TRAINING</text>
  </svg>

  <section class="info-box call">
    <p class="info-label">Call us:</p>
    <p class="phone">410-587-3920</p>
  </section>

  <section class="info-box web">
    <p class="info-label">Web Site:</p>
    <p class="site">www.furlowpaws.com</p>
  </section>

  <div class="band bottom"></div>
  <div class="edge-line bottom"></div>
</main>
</body>
</html>
```